Business Card Design

We require a business card design for a law firm, our signature colours are maroon and cream. Our slogan is "From our family to yours", we would like the cards to be professional however feminine at the same time.

Industry/Entity Type

Business

Contact Information for Business Card

Helena Brockett & Associates Lawyers & Conveyancers, Helena Brockett LL.B. Principal Solicitor, 17 Thornbury Street, Kelvale NSW 2239

Logo styles of interest
Emblem Logo
Abstract Logo
Wordmark Logo

```html
<!DOCTYPE html>
<html lang="en">
<head>
<meta charset="utf-8">
<title>Helena Brockett &amp; Associates – Business Card</title>
<link rel="stylesheet" href="https://fonts.googleapis.com/css2?family=Marcellus&display=swap">
<style>
  :root {
    --backdrop: #eceef0;
    --card-red-light: #e4100f;
    --card-red: #d10808;
    --card-red-dark: #a80000;
    --cream: #ffe0bd;
    --cream-light: #ffe6c9;
    --cream-deep: #fbd2a6;
    --ink-red: #c40c0c;
  }
  * { margin: 0; padding: 0; box-sizing: border-box; }
  html, body {
    width: 1200px;
    height: 864px;
    overflow: hidden;
    background: var(--backdrop);
  }
  .canvas {
    position: relative;
    width: 1200px;
    height: 864px;
  }
  .business-card {
    position: absolute;
    left: 120px;
    top: 144px;
    width: 960px;
    height: 576px;
    overflow: hidden;
    font-family: "Marcellus", "Optima", serif;
    background: radial-gradient(ellipse at 50% 42%, var(--card-red-light) 0%, var(--card-red) 45%, var(--card-red-dark) 100%);
    box-shadow: 0 6px 18px rgba(0, 0, 0, 0.18);
  }
  .holder {
    position: absolute;
    left: 38px;
    top: 30px;
    color: var(--cream);
    font-size: 19px;
    line-height: 1;
    letter-spacing: 0.2px;
  }
  .holder-name { display: block; margin-bottom: 22px; }
  .holder-title { display: block; }
  .firm-mark {
    position: absolute;
    left: 0;
    right: 0;
    top: 150px;
    text-align: center;
    color: var(--cream);
  }
  .firm-mark-dot {
    display: block;
    width: 18px;
    height: 18px;
    margin: 0 auto 22px;
    border-radius: 50%;
    background: var(--cream);
  }
  .firm-mark-name {
    display: block;
    font-size: 34px;
    line-height: 1.1;
  }
  .firm-mark-sub {
    display: block;
    font-size: 21px;
    margin-top: 4px;
  }
  .address-band {
    position: absolute;
    left: 0;
    right: 0;
    top: 398px;
    height: 72px;
    display: flex;
    align-items: center;
    padding: 0 28px;
    background: linear-gradient(90deg, var(--cream-deep), var(--cream-light) 50%, var(--cream-deep));
    color: var(--ink-red);
    font-size: 18.5px;
    white-space: nowrap;
    letter-spacing: 0.1px;
  }
</style>
</head>
<body>
<main class="canvas">
  <article class="business-card">
    <header class="holder">
      <span class="holder-name">Helena Brockett</span>
      <span class="holder-title">LL.B. Principal Solicitor</span>
    </header>
    <div class="firm-mark">
      <span class="firm-mark-dot"></span>
      <span class="firm-mark-name">Helena Brockett &amp; Associates</span>
      <span class="firm-mark-sub">Lawyers</span>
    </div>
    <footer class="address-band">
      Helena Brockett &amp; Associates Lawyers &amp; Conveyancers, 17 Thornbury Street, Kelvale NSW 2239
    </footer>
  </article>
</main>
</body>
</html>
```